Maple Crest Glow Skin Studio needs an 8 page WP redesign

We need a colorful re-design for an 8 page Wordpress website. The current preliminary website is live. The home page URL is http://maplecrestglowskinstudio.example The new logo is live on the website also. I would like a (re)design using the colors that are represented by the new logo file, and any additional complimentary colors. The information regarding the business can be found on the website already, so please review it for insight. The name of the business is "Maple Crest Glow Skin Studio".

Target Market(s)

The targeted website viewer is an adult female between the ages of 30 and 75 who is interested in facial renewal, wart removal and scar removal. This website should inspire in the target viewer the benefits of laser facial renewal, wart removal and new scar removal. Potential website viewers are wanting and searching for improved skin health and appearance. The website must represent the essence of a professional spa business.

Industry/Entity Type

Business

Font styles to use
Sans Serif

Requirements
Must have
• - The phone number placed in a visible and high value widget area that allows mobile phone browser dialing.

```html
<!DOCTYPE html>
<html lang="en">
<head>
<meta charset="utf-8">
<title>Maple Crest Glow Skin Studio</title>
<link rel="stylesheet" href="https://fonts.googleapis.com/css2?family=Michroma&family=Open+Sans:wght@400;600;700&family=Arimo:wght@400;700&display=swap">
<style>
:root{
  --purple:#a3149f;
  --purple-dark:#4a1d45;
  --magenta:#d23bd6;
  --pink:#d36fd4;
  --ink:#2b1b33;
  --hero-a:#7f93a6;
  --hero-b:#a9b8c6;
  --footer:#2a2a2a;
  --field:#3a3a3a;
  --text:#333;
  --muted:#888;
}
*{margin:0;padding:0;box-sizing:border-box}
html,body{width:1200px;height:2169px;overflow:hidden}
body{position:relative;background:#fff;font-family:"Arimo",Arial,sans-serif;color:var(--text)}
.abs{position:absolute}
/* header */
.logo{left:113px;top:26px;width:270px;font-family:"Open Sans",sans-serif;font-weight:700;color:var(--purple-dark);font-size:28px;line-height:32px}
.hinfo{font-family:"Open Sans",sans-serif;font-size:13px;color:#222;line-height:18px}
.hinfo b{font-weight:700;display:block}
.nav{left:0;top:140px;width:1200px;height:48px;background:var(--purple);display:flex;padding-left:98px}
.nav a{color:#fff;text-decoration:none;font-size:15px;line-height:48px;padding:0 26px}
.nav a.active{background:#4b1b47}
/* hero */
.hero{left:0;top:188px;width:1200px;height:419px;background:linear-gradient(90deg,var(--hero-a),var(--hero-b) 60%,#8ea0b2)}
.hero-photo{left:578px;top:188px;width:622px;height:419px;background:radial-gradient(ellipse at 55% 45%,#e9d6cc 0,#c9b1a6 30%,rgba(160,176,192,0) 65%)}
.hero h1{left:137px;top:218px;font-family:"Michroma",sans-serif;font-size:40px;color:var(--ink);letter-spacing:1px}
.hero-box{left:129px;top:288px;width:344px;height:63px;background:rgba(200,208,216,.75);font-family:"Michroma",sans-serif;color:#a51c9f;font-size:38px;line-height:63px;padding-left:14px}
.guarantee{left:131px;top:363px;font-family:"Open Sans",sans-serif;font-size:37px;color:#fff}
.hero-lead{left:137px;top:417px;width:370px;font-size:13px;line-height:20px;color:#fff}
.order{left:134px;top:477px;width:123px;height:55px;border-radius:6px;background:linear-gradient(#f5f5f5,#cfcfcf);border:1px solid #b8b8b8;font-size:17px;color:#333;text-align:center;line-height:53px}
.main-bg{left:0;top:607px;width:1200px;height:1193px;background:linear-gradient(180deg,#eef7fb,#fff 20%,#fff 60%,#e2f1f8 75%,#cfe8f3)}
/* cards */
.card{top:648px;width:212px;height:121px;background:linear-gradient(135deg,#e64ae9,#c02dc3);color:#fff;padding:14px 16px;box-shadow:0 3px 6px rgba(0,0,0,.2);overflow:hidden}
.card h3{font-family:"Open Sans",sans-serif;font-weight:400;font-size:17px}
.card p{font-size:13px;line-height:16px;margin-top:3px;width:190px;opacity:.9}
.card .arrow{position:absolute;right:-12px;bottom:-22px;width:66px;height:66px;border-radius:50%;background:#fff}
.card svg{position:absolute;right:12px;bottom:10px}
/* services */
.svc{left:147px;width:280px;height:80px}
.svc .ic{position:absolute;left:1px;top:0;width:62px;height:62px;border-radius:50%}
.svc .ic svg{position:absolute;left:15px;top:15px}
.svc h4{position:absolute;left:86px;top:-2px;font-family:"Open Sans",sans-serif;font-weight:400;font-size:14px;color:#b0179f}
.svc p{position:absolute;left:86px;top:18px;font-size:13px;line-height:18px;color:#333;width:150px}
.svc .chev{position:absolute;left:238px;top:16px}
.svc .line{position:absolute;left:70px;top:78px;width:220px;height:1px;background:linear-gradient(90deg,#ddd,transparent)}
.vdiv{left:458px;top:812px;width:0;height:535px;border-left:1px dashed #bbb}
.about-copy{left:506px;top:834px;width:308px;font-family:"Open Sans",sans-serif;font-size:13px;line-height:21.7px;color:#333;text-align:justify}
.about-copy p+p{margin-top:22px}
.portrait{left:831px;top:834px;width:226px;height:259px;background:#fff;box-shadow:0 2px 8px rgba(0,0,0,.25)}
.portrait div{position:absolute;left:17px;top:14px;width:192px;height:230px;background:linear-gradient(160deg,#7a5a3e,#a67b5c 45%,#7b2a74)}
.btn-dark{top:1149px;height:39px;background:linear-gradient(#3a3a3a,#111);color:#fff;font-size:14px;line-height:39px;padding-left:22px;box-shadow:0 3px 5px rgba(0,0,0,.3)}
.connect-label{left:567px;top:1281px;font-size:14px;color:#222}
.soc{top:1263px;width:54px;height:54px;border-radius:50%;box-shadow:0 2px 4px rgba(0,0,0,.3)}
.sep{left:130px;top:1381px;width:940px;height:2px;background:linear-gradient(90deg,transparent,#d8e2e8,transparent)}
/* video */
.video{left:240px;top:1414px;width:429px;height:270px;background:#fff;box-shadow:0 3px 8px rgba(0,0,0,.25)}
.video .screen{position:absolute;left:14px;top:12px;width:401px;height:242px;background:#000}
.video .bar{position:absolute;left:0;bottom:0;width:401px;height:24px;background:#1b1b1b}
.video .prog{position:absolute;left:0;top:0;width:295px;height:3px;background:#c00}
.video-caption{left:200px;top:1710px;width:510px;text-align:center;font-size:13px;line-height:19px;color:#222}
.model{left:780px;top:1431px;width:377px;height:369px;background:radial-gradient(ellipse at 45% 45%,#ecd9cf 0,#d6bdb1 30%,rgba(210,232,244,0) 65%)}
/* footer */
.footer{left:0;top:1800px;width:1200px;height:325px;background:var(--footer);border-top:6px solid #777}
.f-logo{left:116px;top:1912px;width:180px;font-family:"Open Sans",sans-serif;font-weight:700;font-size:20px;line-height:24px;color:#fff}
.f-h{font-family:"Open Sans",sans-serif;font-weight:600;font-size:20px;color:var(--pink)}
.f-copy{left:318px;top:1884px;width:252px;font-size:12px;line-height:21px;color:#8a8a8a}
.f-row{left:318px;width:270px;height:40px;border-top:1px solid #3a3a3a;font-size:11px;color:#999}
.f-row span{position:absolute;top:12px}
.f-row .v{left:118px;color:#ccc}
.field{left:604px;width:263px;background:var(--field);border:2px solid #555;border-radius:3px;font-size:11px;color:#aaa;padding:8px 20px}
.submit{left:789px;top:2085px;width:78px;height:33px;background:#444;color:#888;font-size:10px;font-style:italic;text-align:center;line-height:33px}
.thumb{width:74px;height:73px;border:3px solid #555}
.copyright{left:0;top:2125px;width:1200px;height:44px;background:var(--pink);color:#fff;font-size:13px;text-align:center;line-height:44px}
</style>
</head>
<body>

<div class="abs logo">Maple Crest Glow<br>Skin Studio</div>

<svg class="abs" style="left:703px;top:74px" width="32" height="32" viewBox="0 0 32 32"><circle cx="16" cy="16" r="13" fill="none" stroke="#222" stroke-width="3"/><path d="M16 8v9h6" fill="none" stroke="#222" stroke-width="3"/></svg>
<div class="abs hinfo" style="left:743px;top:73px"><b>24HR SHIPPING</b>Free for Customers</div>
<svg class="abs" style="left:922px;top:72px" width="26" height="34" viewBox="0 0 26 34"><path d="M6 2l6 7-4 4c2 5 5 9 10 12l4-4 6 6-4 5C12 30 3 19 2 7z" fill="#222"/></svg>
<div class="abs hinfo" style="left:958px;top:73px"><b>CALL TOLL FREE</b><a href="tel:1800555456" style="color:#222;text-decoration:none">1800 - 555 - GLOWSKIN</a></div>

<nav class="abs nav">
  <a class="active">Home</a><a>About Us</a><a>Skin Renewal</a><a>Scar Removal</a><a>Wart Removal</a><a>Your Visit</a><a>Contact Us</a><a>Blog</a>
</nav>

<section>
  <div class="abs hero"></div>
  <div class="abs hero-photo" role="img" aria-label="Portrait of a woman with clear skin touching her face, with floating white feathers"></div>
  <h1 class="abs" style="left:137px;top:218px;font-family:'Michroma',sans-serif;font-size:40px;color:var(--ink);font-weight:400">Maple Crest Glow</h1>
  <div class="abs hero-box">Skin Renewal</div>
  <div class="abs guarantee">100 % GUARANTEE</div>
  <p class="abs hero-lead">Lorem Ipsum is simply dummy text of the printing and type-setting industry.</p>
  <div class="abs order">ORDER NOW</div>
</section>

<div class="abs main-bg"></div>

<div class="abs card" style="left:147px"><h3>COSMETIC</h3><p>Lorem ipsum dolor sit amet, consectetuer.</p><span class="arrow"></span><svg width="18" height="22" viewBox="0 0 18 22"><path d="M4 2l10 9-10 9" fill="none" stroke="#999" stroke-width="2"/></svg></div>
<div class="abs card" style="left:383px"><h3>MEDICAL</h3><p>Lorem ipsum dolor sit amet, consectetuer.</p><span class="arrow"></span><svg width="18" height="22" viewBox="0 0 18 22"><path d="M4 2l10 9-10 9" fill="none" stroke="#999" stroke-width="2"/></svg></div>
<div class="abs card" style="left:616px"><h3>LASER</h3><p>Lorem ipsum dolor sit amet, consectetuer.</p><span class="arrow"></span><svg width="18" height="22" viewBox="0 0 18 22"><path d="M4 2l10 9-10 9" fill="none" stroke="#999" stroke-width="2"/></svg></div>
<div class="abs card" style="left:847px"><h3>SURGICAL</h3><p>Lorem ipsum dolor sit amet, consectetuer.</p><span class="arrow"></span><svg width="18" height="22" viewBox="0 0 18 22"><path d="M4 2l10 9-10 9" fill="none" stroke="#999" stroke-width="2"/></svg></div>

<div class="abs svc" style="top:829px"><span class="ic" style="background:#e0496a"><svg width="32" height="32" viewBox="0 0 32 32"><path d="M16 28C4 19 2 13 5 8c3-4 8-3 11 1 3-4 8-5 11-1 3 5 1 11-11 20z" fill="#fff"/></svg></span><h4>ABOUT US</h4><p>Lorem ipsum dolor sit amet, consectetuer.</p><svg class="chev" width="18" height="28" viewBox="0 0 18 28"><path d="M3 3l11 11-11 11" fill="none" stroke="#ddd" stroke-width="2"/></svg><span class="line"></span></div>
<div class="abs svc" style="top:929px"><span class="ic" style="background:#3fa8c4"><svg width="32" height="32" viewBox="0 0 32 32"><rect x="2" y="10" width="28" height="12" rx="4" fill="#fff"/><rect x="12" y="12" width="8" height="8" fill="#3fa8c4"/></svg></span><h4>MOHS SURGERY</h4><p>Lorem ipsum dolor sit amet, consectetuer.</p><svg class="chev" width="18" height="28" viewBox="0 0 18 28"><path d="M3 3l11 11-11 11" fill="none" stroke="#ddd" stroke-width="2"/></svg><span class="line"></span></div>
<div class="abs svc" style="top:1035px"><span class="ic" style="background:#4fb89a"><svg width="32" height="32" viewBox="0 0 32 32"><rect x="3" y="9" width="26" height="19" rx="3" fill="#fff"/><rect x="11" y="4" width="10" height="6" fill="none" stroke="#fff" stroke-width="2"/><path d="M16 13v11M10.5 18.5h11" stroke="#4fb89a" stroke-width="3"/></svg></span><h4>INSURANCE</h4><p>Lorem ipsum dolor sit amet, consectetuer.</p><svg class="chev" width="18" height="28" viewBox="0 0 18 28"><path d="M3 3l11 11-11 11" fill="none" stroke="#ddd" stroke-width="2"/></svg><span class="line"></span></div>
<div class="abs svc" style="top:1140px"><span class="ic" style="background:#f3b523"><svg width="32" height="32" viewBox="0 0 32 32"><circle cx="9" cy="19" r="6" fill="none" stroke="#fff" stroke-width="3"/><circle cx="23" cy="19" r="6" fill="none" stroke="#fff" stroke-width="3"/><path d="M14 18h4M4 14l3-7M28 14l-3-7" stroke="#fff" stroke-width="3"/></svg></span><h4>PATIENT RESOURCES</h4><p>Lorem ipsum dolor sit amet, consectetuer.</p><svg class="chev" width="18" height="28" viewBox="0 0 18 28"><path d="M3 3l11 11-11 11" fill="none" stroke="#ddd" stroke-width="2"/></svg><span class="line"></span></div>
<div class="abs svc" style="top:1249px"><span class="ic" style="background:#3fa8c4"><svg width="32" height="32" viewBox="0 0 32 32"><path d="M2 10h18v14H2zM20 14h6l4 5v5H20z" fill="#fff"/><circle cx="8" cy="25" r="3" fill="#3fa8c4"/><circle cx="24" cy="25" r="3" fill="#3fa8c4"/><path d="M11 12v9M6.5 16.5h9" stroke="#3fa8c4" stroke-width="2.5"/></svg></span><h4>CONTACT US</h4><p>Lorem ipsum dolor sit amet, consectetuer.</p><svg class="chev" width="18" height="28" viewBox="0 0 18 28"><path d="M3 3l11 11-11 11" fill="none" stroke="#ddd" stroke-width="2"/></svg></div>

<div class="abs vdiv"></div>

<div class="abs about-copy">
  <p>It was popularised in the 1960s with the release of Letraset sheets containing Lorem Ipsum passages, and more recently with desktop publishing the release of Letraset sheets containing Lorem Ipsum passages, and m<br>ore recently with desktop</p>
  <p>Publishing the release of Letraset sheets containing Lorem Ipsum passages, and more recently with desktop publishing software like Aldus PageMaker including versions of Lorem Ipsum.It was popularised in the 1960s with the release.</p>
</div>
<div class="abs portrait"><div role="img" aria-label="Portrait photo of the studio's lead doctor"></div></div>

<div class="abs btn-dark" style="left:507px;width:161px">CONNECT &gt;</div>
<div class="abs btn-dark" style="left:685px;width:170px">FOLLOW ME &nbsp;&gt;</div>
<div class="abs btn-dark" style="left:873px;width:185px">MEET DR. HARTWELL &nbsp;&gt;</div>

<div class="abs connect-label">CONNECT WITH US</div>
<span class="abs soc" style="left:732px;background:#333"></span>
<span class="abs soc" style="left:804px;background:#c8232c"></span>
<span class="abs soc" style="left:871px;background:#2f5597"></span>
<span class="abs soc" style="left:942px;background:#3ba7d8"></span>

<div class="abs sep"></div>

<div class="abs model" role="img" aria-label="Photo of a woman with glowing skin touching her cheek"></div>
<div class="abs video">
  <div class="screen">
    <svg style="position:absolute;left:140px;top:45px" width="122" height="122" viewBox="0 0 122 122"><circle cx="61" cy="61" r="58" fill="#2a2a2a" stroke="#444" stroke-width="4"/><path d="M46 36l42 25-42 25z" fill="#111"/></svg>
    <div class="bar"><div class="prog"></div></div>
  </div>
</div>
<p class="abs video-caption">Lorem ipsum dolor sit amet, consectetuer adipiscing elit, sed diam nonummy nibh euismod tincidunt ut laoreet dolore magna aliquam erat volutpat.</p>

<footer>
  <div class="abs footer"></div>
  <div class="abs f-logo">Maple Crest Glow<br>Skin Studio</div>
  <h4 class="abs f-h" style="left:318px;top:1836px">Our Location</h4>
  <p class="abs f-copy">Lorem ipsum dolor sit amet ne onsectetuer adsi tashinipiscing elit. Aenean commodo ligula egtt ashin dolor in tashin tyon.</p>
  <div class="abs f-row" style="top:1982px"><span style="left:25px">BY E-MAIL;</span><span class="v">info@maplecrestglow.example</span></div>
  <div class="abs f-row" style="top:2022px"><span style="left:25px">BY PHONE;</span><span class="v"><a href="tel:+90055501" style="color:#ccc;text-decoration:none">+900-55501</a></span></div>
  <div class="abs f-row" style="top:2062px"><span style="left:25px">ADDRESS;</span><span class="v" style="width:140px;line-height:13px">45, Birchwood Lane, Fern Vale, USA</span></div>
  <svg class="abs" style="left:318px;top:1995px" width="14" height="12" viewBox="0 0 14 12"><rect x="1" y="1" width="12" height="10" fill="none" stroke="#999"/><path d="M1 1l6 5 6-5" fill="none" stroke="#999"/></svg>
  <svg class="abs" style="left:318px;top:2036px" width="14" height="14" viewBox="0 0 14 14"><path d="M3 1l3 3-2 2c1 2 2 3 4 4l2-2 3 3-2 2C6 12 2 8 1 3z" fill="#999"/></svg>
  <svg class="abs" style="left:318px;top:2076px" width="14" height="14" viewBox="0 0 14 14"><path d="M1 7l6-5 6 5M3 6v7h8V6" fill="#999"/></svg>

  <h4 class="abs f-h" style="left:600px;top:1835px">Contact Now</h4>
  <div class="abs field" style="top:1888px;height:32px">Name</div>
  <div class="abs field" style="top:1933px;height:31px">Email</div>
  <div class="abs field" style="top:1976px;height:96px">Message</div>
  <div class="abs submit">SUBMIT</div>

  <h4 class="abs f-h" style="left:893px;top:1842px">Our Gallery</h4>
  <div class="abs thumb" style="left:898px;top:1892px;background:linear-gradient(#8fa3b4,#6b6f66)" role="img" aria-label="Gallery photo of a street scene"></div>
  <div class="abs thumb" style="left:993px;top:1892px;background:linear-gradient(135deg,#9bbd6a,#c7544b)" role="img" aria-label="Gallery photo of a fresh salad"></div>
  <div class="abs thumb" style="left:898px;top:1986px;background:linear-gradient(#6f93b8,#d8dde2 60%,#333)" role="img" aria-label="Gallery photo of a cloudy sky"></div>
  <div class="abs thumb" style="left:993px;top:1986px;background:linear-gradient(135deg,#6e6a5e,#b8b2a0)" role="img" aria-label="Gallery photo of a stone statue"></div>

  <div class="abs copyright">Copyright © 2014 maplecrestglowskinstudio.example, . All rights reserved.</div>
</footer>

</body>
</html>
```